Carpet cleaning company wants business card

Need an exciting new fresh design for business cards for my carpet cleaning /pest control business
www.brightwovecare.com.au
Can design include a lined section for quoting or information? Thanks !

```html
<!DOCTYPE html>
<html lang="en">
<head>
<meta charset="utf-8">
<title>BrightWove Care – Business Card</title>
<link rel="stylesheet" href="https://fonts.googleapis.com/css2?family=Roboto:wght@400;700;900&display=swap">
<style>
  :root {
    --page: #e9e6e2;
    --blue-deep: #0f4f96;
    --blue-mid: #1e6cc0;
    --blue-light: #3a86d4;
    --red: #d9322b;
    --red-dark: #b3211c;
    --white: #ffffff;
    --scene-sky: #b9cfe0;
    --scene-van: #e6e9ec;
    --scene-road: #8f9498;
  }
  html, body {
    margin: 0;
    width: 1200px;
    height: 1054px;
    overflow: hidden;
    background: var(--page);
    font-family: "Roboto", Arial, sans-serif;
  }
  .card {
    position: absolute;
    left: 100px;
    top: 225px;
    width: 1000px;
    height: 603px;
    border-radius: 26px;
    overflow: hidden;
    box-shadow: 0 12px 40px rgba(0,0,0,0.18);
  }
  .card-art {
    position: absolute;
    inset: 0;
    width: 1000px;
    height: 603px;
  }
  .brand {
    position: absolute;
    left: 52px;
    top: 62px;
    display: flex;
    align-items: center;
    gap: 14px;
    color: var(--white);
    font-weight: 900;
    font-size: 54px;
    letter-spacing: -1px;
    line-height: 1;
  }
  .brand-dot {
    width: 26px;
    height: 26px;
    border-radius: 50%;
    background: var(--red);
  }
  .main-call {
    position: absolute;
    left: 52px;
    top: 312px;
    color: var(--white);
    font-weight: 700;
    font-size: 38px;
    letter-spacing: 0.5px;
  }
  .contacts {
    position: absolute;
    left: 52px;
    top: 378px;
    margin: 0;
    padding: 0;
    list-style: none;
    color: var(--white);
    font-size: 24px;
  }
  .contacts li {
    display: flex;
    align-items: center;
    gap: 20px;
    height: 36px;
  }
  .contacts svg {
    width: 22px;
    height: 22px;
    fill: var(--white);
  }
  .services {
    position: absolute;
    left: 50px;
    top: 526px;
    color: #f7d7d5;
    font-size: 25px;
    letter-spacing: 0.2px;
  }
  .services .sep { margin: 0 16px; }
</style>
</head>
<body>
  <div class="card">
    <svg class="card-art" viewBox="0 0 1000 603" aria-hidden="false">
      <defs>
        <linearGradient id="panelBlue" x1="0" y1="0" x2="1" y2="1">
          <stop offset="0" stop-color="#2a79c9"/>
          <stop offset="0.55" stop-color="#1c62b0"/>
          <stop offset="1" stop-color="#0f4f96"/>
        </linearGradient>
        <linearGradient id="sceneTone" x1="0" y1="0" x2="0" y2="1">
          <stop offset="0" stop-color="#bcd2e4"/>
          <stop offset="0.5" stop-color="#e4e7ea"/>
          <stop offset="1" stop-color="#8e9397"/>
        </linearGradient>
      </defs>
      <rect class="panel" width="1000" height="603" fill="url(#panelBlue)"/>
      <path class="service-band" d="M0 521 H545 L560 569 H0 Z" fill="var(--red)"/>
      <path class="curve-red" d="M588 0 C515 170 500 400 618 603 H650 C540 400 555 170 612 0 Z" fill="var(--red)"/>
      <path class="team-scene" role="img" aria-label="Illustration of two cleaning technicians standing in front of the company van"
            d="M612 0 C555 170 540 400 650 603 H1000 V0 Z" fill="url(#sceneTone)"/>
    </svg>

    <div class="brand"><span class="brand-dot"></span>BrightWove Care</div>

    <div class="main-call">CALL: 07-5120-4870</div>

    <ul class="contacts">
      <li>
        <svg viewBox="0 0 24 24"><path d="M6.6 10.8c1.4 2.8 3.8 5.1 6.6 6.6l2.2-2.2c.3-.3.7-.4 1-.2 1.1.4 2.3.6 3.6.6.6 0 1 .4 1 1V20c0 .6-.4 1-1 1C10.6 21 3 13.4 3 4c0-.6.4-1 1-1h3.5c.6 0 1 .4 1 1 0 1.3.2 2.5.6 3.6.1.3 0 .7-.2 1z"/></svg>
        <span>0412 560 294</span>
      </li>
      <li>
        <svg viewBox="0 0 24 24"><path d="M2 5h20v14H2z M3.5 6.5 12 13l8.5-6.5" fill="none" stroke="#fff" stroke-width="2"/></svg>
        <span>admin@brightwovecare.com.au</span>
      </li>
      <li>
        <svg viewBox="0 0 24 24"><circle cx="12" cy="12" r="9" fill="none" stroke="#fff" stroke-width="2"/><path d="M3 12h18M12 3c3 3 3 15 0 18M12 3c-3 3-3 15 0 18" fill="none" stroke="#fff" stroke-width="1.6"/></svg>
        <span>www.brightwovecare.com.au</span>
      </li>
    </ul>

    <div class="services">Carpet Cleaning<span class="sep">|</span>Pest control</div>
  </div>
</body>
</html>
```